Silver Creek Plumbing Business card & letter head design

We need a new business card and letter head for our plumbing company called silver creek plumbing. attached is the companys logo. We provide domestic and commercial plumbing services in regional western Australia. We are after Something simple yet nice to look at and something that fits within the trade industry.

Target Market(s)

trade/building industry

Contact Information for Business Card

Darl Hensby
Manager
0461 238 574
enquiries@scplumbwork.net.au
ABN: 47 381 905 462
PCL: 5187

Domestic & Commercial Plumbing
Tip Truck & Excavator hire

Colors

Designer to choose colors to be used in the design.

```html
<!DOCTYPE html>
<html lang="en">
<head>
<meta charset="utf-8">
<title>Silver Creek Plumbing – Business Card</title>
<link rel="stylesheet" href="https://fonts.googleapis.com/css2?family=Roboto:wght@300;400;700&display=swap">
<style>
  :root {
    --brand-blue: #1256a7;
    --text-grey: #555a60;
    --card-white: #ffffff;
    --page-bg: #e6e6e6;
  }
  * { margin: 0; padding: 0; box-sizing: border-box; }
  html, body { width: 1125px; height: 1200px; overflow: hidden; background: var(--page-bg); }
  body { position: relative; font-family: "Roboto", Arial, sans-serif; }

  .card {
    position: absolute;
    left: 150px;
    width: 825px;
    height: 471px;
    border-radius: 24px;
  }
  .card--front { top: 98px; background: var(--card-white); }
  .card--back { top: 631px; background: var(--brand-blue); color: #fff; }

  .wordmark { position: absolute; text-align: center; font-weight: 700; line-height: 1; }
  .wordmark__line { display: block; }
  .card--front .wordmark { left: 82px; top: 196px; width: 300px; color: var(--brand-blue); }
  .card--front .wordmark__name { font-size: 36px; letter-spacing: -0.5px; }
  .card--front .wordmark__trade { font-size: 17px; letter-spacing: 6px; margin-top: 8px; }

  .divider {
    position: absolute; left: 412px; top: 139px;
    width: 2px; height: 192px; background: var(--brand-blue);
  }

  .contact { position: absolute; left: 452px; top: 128px; color: var(--text-grey); }
  .contact__name { font-size: 30px; font-weight: 700; color: var(--brand-blue); letter-spacing: 0.3px; }
  .contact__role { font-size: 20px; margin-top: 2px; }
  .contact__ids { margin-top: 22px; font-size: 21px; line-height: 26px; }
  .contact__label { color: var(--brand-blue); }
  .contact__lines { margin-top: 18px; font-size: 21px; line-height: 27px; }
  .contact__row { display: flex; align-items: center; gap: 10px; }
  .contact__row svg { width: 18px; height: 18px; fill: var(--brand-blue); flex: none; }

  .card--back .wordmark { left: 0; width: 825px; top: 168px; }
  .card--back .wordmark__name { font-size: 64px; letter-spacing: -1px; }
  .card--back .wordmark__trade { font-size: 32px; letter-spacing: 11px; margin-top: 14px; }

  .services {
    position: absolute; left: 0; width: 825px; top: 375px;
    text-align: center; font-size: 24px; font-weight: 300; line-height: 30px;
  }
</style>
</head>
<body>
  <section class="card card--front">
    <div class="wordmark">
      <span class="wordmark__line wordmark__name">SILVER CREEK</span>
      <span class="wordmark__line wordmark__trade">PLUMBING</span>
    </div>
    <div class="divider"></div>
    <div class="contact">
      <div class="contact__name">DARL HENSBY</div>
      <div class="contact__role">Manager</div>
      <div class="contact__ids">
        <div><span class="contact__label">ABN:</span> 47 381 905 462</div>
        <div><span class="contact__label">PCL:</span> 5187</div>
      </div>
      <div class="contact__lines">
        <div class="contact__row">
          <svg viewBox="0 0 24 24" aria-hidden="true"><path d="M6.6 10.8a15.1 15.1 0 0 0 6.6 6.6l2.2-2.2a1 1 0 0 1 1-.25 11.4 11.4 0 0 0 3.6.57 1 1 0 0 1 1 1V20a1 1 0 0 1-1 1A17 17 0 0 1 3 4a1 1 0 0 1 1-1h3.5a1 1 0 0 1 1 1c0 1.25.2 2.45.57 3.6a1 1 0 0 1-.25 1z"/></svg>
          <span>0461 238 574</span>
        </div>
        <div class="contact__row">
          <svg viewBox="0 0 24 24" aria-hidden="true"><path d="M2 5h20v14H2z M2 5l10 8 10-8" fill="none" stroke="#1256a7" stroke-width="0"/><path d="M2 5h20v1.5l-10 7.5L2 6.5z"/><path d="M2 8.5l10 7.5 10-7.5V19H2z"/></svg>
          <span>enquiries@scplumbwork.net.au</span>
        </div>
      </div>
    </div>
  </section>

  <section class="card card--back">
    <div class="wordmark">
      <span class="wordmark__line wordmark__name">SILVER CREEK</span>
      <span class="wordmark__line wordmark__trade">PLUMBING</span>
    </div>
    <div class="services">
      <div>Domestic &amp; Commercial Plumbing</div>
      <div>Tip Truck &amp; Excavator hire</div>
    </div>
  </section>
</body>
</html>
```